BEACON CABS

Taxi card design

Need changes very slow in replying to my messages.

Target Market(s)

Customers

Industry/Entity Type

Taxi

Contact Information for Business Card

See previous design

Font styles to use
Sans Serif

Colors
A7469A
B969AE
D3A5CF
EDDBEB
F8F0F9
6B429C
8869AF
B7A5CE
E3DAEB
F3F0F8

Requirements
Nice to have
• We are in the business of looking after people, not just driving vehicles front
Should not have
• Front number 01632 480 480 needs to big big

```html
<!DOCTYPE html>
<html lang="en">
<head>
<meta charset="utf-8">
<title>Beacon Cabs – Business Card</title>
<link href="https://fonts.googleapis.com/css2?family=Montserrat:wght@400;500;600;700;800&display=swap" rel="stylesheet">
<style>
  :root{
    --stage:#666666;
    --white:#ffffff;
    --paper:#f8f0f9;
    --ink:#111111;
    --ink-soft:#2b2b2b;
    --magenta:#a0358f;
    --plum:#5e2b7e;
    --plum-deep:#3e1d5e;
    --violet:#6b429c;
  }
  *{box-sizing:border-box;margin:0;padding:0}
  html,body{width:1200px;height:1200px;overflow:hidden;background:var(--stage)}
  body{position:relative;font-family:'Montserrat',sans-serif}
  .card{position:absolute;left:148px;width:903px;height:517px;overflow:hidden;background:var(--white)}
  .card--front{top:60px}
  .card--back{top:623px}
  .card__shapes{position:absolute;inset:0;width:100%;height:100%}
  .abs{position:absolute}

  /* front */
  .brand-vertical{left:103px;top:258px;transform:translate(-50%,-50%) rotate(90deg);white-space:nowrap;
    font-weight:800;font-size:52px;color:var(--ink);letter-spacing:1px}
  .hours{left:358px;top:30px;font-weight:700;font-size:64px;color:var(--white);letter-spacing:1px}
  .services{left:583px;top:29px;width:206px;list-style:none}
  .services li{height:32px;margin-bottom:8px;background:var(--paper);color:var(--plum);
    display:flex;align-items:center;justify-content:center;font-size:17.5px;font-weight:400;white-space:nowrap}
  .services li.wide{font-size:22px}
  .hotline{left:401px;top:158px;display:flex;align-items:center;gap:7px}
  .hotline__number{font-weight:700;font-size:42px;color:var(--white);letter-spacing:3px}
  .pill{top:220px;width:188px;height:29px;background:var(--paper);border-radius:18px 3px 18px 3px;
    display:flex;align-items:center;justify-content:center;font-weight:700;font-size:16.5px;color:var(--ink);letter-spacing:2px}
  .contact{left:413px;display:flex;align-items:flex-start;gap:12px;color:var(--white);font-size:24px;line-height:30px;font-weight:400;letter-spacing:.5px}
  .contact svg{flex:none;margin-top:5px}
  .contact--address{top:269px}
  .contact--mobile{top:394px}
  .contact--mail{top:431px}

  /* back */
  .website{left:72px;top:259px;transform:translate(-50%,-50%) rotate(90deg);white-space:nowrap;
    font-weight:700;font-size:24px;color:var(--white);letter-spacing:.5px}
  .brand-main{left:550px;top:234px;transform:translate(-50%,-50%);white-space:nowrap;
    font-weight:800;font-size:64px;color:var(--ink);letter-spacing:1px}
  .back-phone{left:550px;top:329px;transform:translate(-50%,-50%);display:flex;align-items:center;gap:12px}
  .back-phone__number{font-weight:700;font-size:36px;color:var(--ink-soft);letter-spacing:1px;white-space:nowrap}
</style>
</head>
<body>

<section class="card card--front" aria-label="Business card front">
  <svg class="card__shapes" viewBox="0 0 1454 832" preserveAspectRatio="none" aria-hidden="true">
    <defs>
      <linearGradient id="panelFront" x1="0" y1="0" x2="1" y2="0">
        <stop offset="0.35" stop-color="#a0358f"/>
        <stop offset="0.75" stop-color="#6a2c84"/>
        <stop offset="1" stop-color="#5e2b7e"/>
      </linearGradient>
      <linearGradient id="stripeFront" x1="0" y1="0" x2="1" y2="0">
        <stop offset="0" stop-color="#5e2b80"/>
        <stop offset="1" stop-color="#3e1d5e"/>
      </linearGradient>
    </defs>
    <polygon points="464,0 1454,0 1454,832 474,832 258,436" fill="url(#stripeFront)"/>
    <polygon points="541,0 1454,0 1454,832 551,832 336,436" fill="url(#panelFront)"/>
  </svg>

  <div class="abs brand-vertical">BEACON CABS</div>
  <div class="abs hours">24/7</div>
  <ul class="abs services">
    <li>AIRPORT TRANSFERS</li>
    <li class="wide">MINIBUSES</li>
    <li>SCHOOL TRANSPORT</li>
  </ul>

  <div class="abs hotline">
    <svg width="38" height="42" viewBox="0 0 38 42" aria-hidden="true">
      <polygon points="19,1 36,11 36,31 19,41 2,31 2,11" fill="var(--white)"/>
      <path d="M13 12c1.5-1 3-1 3.5 0l2 4c.4.8 0 1.6-.7 2l-1.3.8c.8 2.2 2.4 4 4.4 5.2l1.1-1c.6-.6 1.5-.6 2.1 0l3 3c.6.7.4 1.8-.5 2.5-1.5 1.2-3.5 1.4-5.3.5-4.2-2.2-7.4-6-8.8-10.6-.5-2.3.4-4.9 2.5-6.4z" fill="var(--plum)"/>
    </svg>
    <span class="hotline__number">01632 480 777</span>
  </div>

  <div class="abs pill" style="left:271px">01632 48 66 66</div>
  <div class="abs pill" style="left:478px">091632 20 20 20</div>
  <div class="abs pill" style="left:684px">091632 48 88 11</div>

  <div class="abs contact contact--address">
    <svg width="22" height="22" viewBox="0 0 22 22" aria-hidden="true">
      <circle cx="11" cy="11" r="11" fill="var(--white)"/>
      <path d="M11 4.5a4.5 4.5 0 0 0-4.5 4.5c0 3.2 4.5 8 4.5 8s4.5-4.8 4.5-8A4.5 4.5 0 0 0 11 4.5z" fill="var(--magenta)"/>
      <circle cx="11" cy="9" r="1.8" fill="var(--white)"/>
    </svg>
    <address style="font-style:normal">St. Marys Parish Hall<br>Market Row<br>Hillbrook<br>HB12 3XZ</address>
  </div>
  <div class="abs contact contact--mobile">
    <svg width="22" height="22" viewBox="0 0 22 22" aria-hidden="true">
      <circle cx="11" cy="11" r="11" fill="var(--white)"/>
      <rect x="7.5" y="4.5" width="7" height="13" rx="1.2" fill="var(--plum)"/>
      <rect x="8.7" y="6" width="4.6" height="9" fill="var(--white)"/>
    </svg>
    <span>08000480480</span>
  </div>
  <div class="abs contact contact--mail">
    <svg width="22" height="22" viewBox="0 0 22 22" aria-hidden="true">
      <circle cx="11" cy="11" r="11" fill="var(--white)"/>
      <rect x="5.5" y="7" width="11" height="8" fill="none" stroke="var(--plum)" stroke-width="1.2"/>
      <path d="M5.5 7l5.5 4.5L16.5 7" fill="none" stroke="var(--plum)" stroke-width="1.2"/>
    </svg>
    <span>beaconcabs@inbox.co.uk</span>
  </div>
</section>

<section class="card card--back" aria-label="Business card back">
  <svg class="card__shapes" viewBox="0 0 1454 832" preserveAspectRatio="none" aria-hidden="true">
    <defs>
      <linearGradient id="panelBack" x1="0" y1="0" x2="1" y2="0">
        <stop offset="0" stop-color="#6b2d88"/>
        <stop offset="0.3" stop-color="#a0358f"/>
      </linearGradient>
      <linearGradient id="stripeBack" x1="0" y1="0" x2="1" y2="0">
        <stop offset="0" stop-color="#3e1d5e"/>
        <stop offset="0.35" stop-color="#5e2b80"/>
      </linearGradient>
    </defs>
    <polygon points="0,0 541,0 336,436 551,832 0,832" fill="url(#stripeBack)"/>
    <polygon points="0,0 464,0 258,436 471,832 0,832" fill="url(#panelBack)"/>
  </svg>

  <div class="abs website">www.hillbrookcabs.co.uk</div>
  <div class="abs brand-main">BEACON CABS</div>
  <div class="abs back-phone">
    <svg width="28" height="31" viewBox="0 0 38 42" aria-hidden="true">
      <polygon points="19,1 36,11 36,31 19,41 2,31 2,11" fill="var(--ink-soft)"/>
      <path d="M13 12c1.5-1 3-1 3.5 0l2 4c.4.8 0 1.6-.7 2l-1.3.8c.8 2.2 2.4 4 4.4 5.2l1.1-1c.6-.6 1.5-.6 2.1 0l3 3c.6.7.4 1.8-.5 2.5-1.5 1.2-3.5 1.4-5.3.5-4.2-2.2-7.4-6-8.8-10.6-.5-2.3.4-4.9 2.5-6.4z" fill="var(--white)"/>
    </svg>
    <span class="back-phone__number">01632 480 480</span>
  </div>
</section>

</body>
</html>
```